Webshop for baby shoes need new design

We are an innovative company selling a one of a kind product on a market with tough competition. We are looking to step up our business and need a new design for our shop.

We are looking for recognition as well as originality. The customer must immediately be able to identify navigation, shopping cart, buy buttons etc. We want warm welcoming colors, but not too strong as to not draw attention away from the products. Retro might be interesting, if "done right".

Suggested color palette: http://huepickerlab.example/#7r2kQmVx9a0b1

We have a logo (attached), but if you have a better idea we might go for that instead. Also, a couple of product images are attached for you to use in the design.

What we do NOT want is a shop that looks like a free template (tradeCart etc). Also, while we are selling baby shoes, we don't want to use the very worn our baby pink/blue scheme, so stay clear of this, thanks.

We suggest that you use this palette, or similar: http://huepickerlab.example/#7r2kQmVx9a0b1

Reason: We feel that we are getting closer to finding a design that we like, but there is still a bit to go. Also we want to give the chance to any late starters to show their idea. The competition is still open.

Target Market(s)

babies and their parents

Industry/Entity Type

Shopping

Requirements
Must have
• The usual webshop elements
- shopping cart
- product listing
- product page
- buy buttons
Nice to have
• - large footer area for links, info and function (see vimlo.example for an example)
- some kind of product navigation/filter (left, top or right)
- place for promotion banners

```html
<!DOCTYPE html>
<html lang="en">
<head>
<meta charset="utf-8">
<title>Pattelo – Baby Shoes</title>
<link href="https://fonts.googleapis.com/css2?family=Questrial&family=Didact+Gothic&display=swap" rel="stylesheet">
<style>
  :root {
    --paper: #f4f1e8;
    --paper-edge: #e9e3d5;
    --brown: #5a2d0c;
    --brown-dark: #3f1f08;
    --brown-tab: #6a3512;
    --ink: #4a4852;
    --band: #e6e0d8;
    --card: #ffffff;
    --dot-off: #d9d9d9;
    --line: #d2c8b8;
  }
  * { margin: 0; padding: 0; box-sizing: border-box; }
  html, body { width: 1200px; height: 1145px; overflow: hidden; }
  body {
    background: var(--paper);
    font-family: "Questrial", "Didact Gothic", sans-serif;
    color: var(--brown);
    position: relative;
  }
  .top-stripe, .bottom-stripe {
    position: absolute; left: 0; width: 1200px; background: var(--brown);
  }
  .top-stripe { top: 0; height: 4px; }
  .bottom-stripe { bottom: 0; height: 6px; }

  .site-header {
    position: absolute; top: 0; left: 0; width: 1200px; height: 101px;
    border-bottom: 1px dashed var(--line);
    box-shadow: 0 2px 0 var(--paper-edge);
  }
  .brand {
    position: absolute; left: 167px; top: 18px; height: 55px;
    display: flex; align-items: center; gap: 12px;
  }
  .brand-square {
    width: 78px; height: 55px; background: var(--brown-tab); border-radius: 6px;
  }
  .brand-name {
    font-size: 42px; font-weight: 400; color: var(--brown-tab); letter-spacing: 1px;
  }
  .main-nav a {
    position: absolute; top: 32px; font-size: 15px; color: var(--brown-dark);
    text-decoration: none; letter-spacing: 0.2px;
  }
  .nav-tab {
    position: absolute; left: 606px; top: 4px; width: 73px; height: 75px;
  }
  .main-nav a.is-active { color: #fff; left: 620px; }

  .hero {
    position: absolute; left: 184px; top: 129px; width: 831px; height: 258px;
    background: var(--card); border-radius: 10px;
    box-shadow: 0 1px 6px rgba(90,60,30,0.18);
  }
  .hero-quote {
    position: absolute; left: 27px; top: 40px; width: 390px;
    color: var(--ink); font-size: 32px; line-height: 40px; text-align: right;
  }
  .hero-quote .big { font-size: 44px; }
  .hero-link {
    position: absolute; left: 150px; top: 174px; font-size: 17px; color: var(--brown);
    text-decoration: none;
  }
  .hero-dots { position: absolute; left: 29px; top: 232px; display: flex; gap: 7px; }
  .hero-dots span { width: 15px; height: 13px; background: var(--dot-off); }
  .hero-dots span.is-current { background: var(--brown); border: 2px solid #e6d6c6; }
  .hero-photo {
    position: absolute; left: 452px; top: 9px; width: 360px; height: 227px;
    background: radial-gradient(ellipse at 50% 55%, #3c3f78 0%, #6f8fc4 45%, #ffffff 75%);
    border-radius: 8px;
  }

  .testimonial {
    position: absolute; left: 180px; top: 413px; width: 840px;
    text-align: center; font-size: 15px; line-height: 22px; color: var(--brown);
  }

  .section-head {
    position: absolute; left: 188px; top: 473px; width: 820px; height: 30px;
    border-bottom: 1px dashed var(--line);
  }
  .section-head .band-left { position: absolute; left: 0; top: 0; width: 27px; height: 28px; background: var(--band); }
  .section-head .band-right { position: absolute; left: 203px; top: 0; right: 0; height: 28px; background: var(--band); border-radius: 0 14px 14px 0; }
  .section-head h2 {
    position: absolute; left: 34px; top: 2px; font-size: 20px; font-weight: 700;
    font-family: "Didact Gothic", sans-serif; color: #1a1208;
  }

  .product-card {
    position: absolute; width: 178px; height: 231px; background: var(--card);
    box-shadow: 0 1px 4px rgba(90,60,30,0.12); text-align: center;
  }
  .product-photo {
    position: absolute; left: 9px; top: 12px; width: 160px; height: 112px; border-radius: 6px;
  }
  .photo-navy { background: radial-gradient(ellipse at 50% 55%, #323a78 0%, #6c94cf 50%, #ffffff 78%); }
  .photo-zip { background: radial-gradient(ellipse at 50% 55%, #2f3770 0%, #c9743a 48%, #ffffff 78%); }
  .photo-teal { background: radial-gradient(ellipse at 50% 55%, #1f5f78 0%, #3f8aa0 50%, #ffffff 78%); }
  .product-name {
    position: absolute; left: 0; width: 100%; top: 149px;
    font-size: 15px; line-height: 17px; color: var(--brown);
  }
  .product-price {
    position: absolute; left: 0; width: 100%; top: 192px;
    font-size: 28px; color: var(--brown-dark);
  }

  .site-footer {
    position: absolute; left: 181px; top: 1086px; width: 837px;
    border-top: 1px solid var(--line); font-family: Arial, sans-serif;
    font-size: 11px; color: var(--brown);
  }
  .site-footer .legal { position: absolute; left: 0; top: 22px; }
  .site-footer .links { position: absolute; right: 0; top: 22px; }
  .site-footer a { color: var(--brown); text-decoration: none; }
</style>
</head>
<body>
  <div class="top-stripe"></div>

  <header class="site-header">
    <div class="brand">
      <span class="brand-square"></span>
      <span class="brand-name">Pattelo</span>
    </div>
    <svg class="nav-tab" viewBox="0 0 73 75" aria-hidden="true">
      <path d="M0 0 H73 V75 L36.5 62 L0 75 Z" fill="#6a3512"/>
      <circle cx="27" cy="14" r="2.5" fill="#8a5530"/>
      <circle cx="36.5" cy="14" r="2.5" fill="#8a5530"/>
      <circle cx="46" cy="14" r="2.5" fill="#8a5530"/>
    </svg>
    <nav class="main-nav">
      <a href="#" class="is-active">HOME</a>
      <a href="#" style="left:697px">ABOUT</a>
      <a href="#" style="left:771px">PRODUCTS</a>
      <a href="#" style="left:881px">CART</a>
      <a href="#" style="left:948px">CONTACT</a>
    </nav>
  </header>

  <section class="hero">
    <p class="hero-quote">“It’s time to Renew Your<br><span class="big">Style</span> with us . . .”</p>
    <a class="hero-link" href="#">Browse Our Latest Collection &gt;</a>
    <div class="hero-dots"><span class="is-current"></span><span></span><span></span><span></span></div>
    <div class="hero-photo" role="img" aria-label="Pair of navy and light blue baby sneakers"></div>
  </section>

  <p class="testimonial">“Lorem ipsum dolor sit amet, consectetuer adipiscing elit, sed diam nonummy nibh euismod tincidunt ut<br>laoreet dolore magna aliquam erat volutpat” Testimonial By - Rowan D</p>

  <div class="section-head">
    <span class="band-left"></span>
    <h2>This is our Style</h2>
    <span class="band-right"></span>
  </div>

  <article class="product-card" style="left:202px;top:526px"><div class="product-photo photo-navy" role="img" aria-label="Navy lace-up baby sneaker"></div><p class="product-name">Product Name Or<br>Number</p><p class="product-price">$399</p></article>
  <article class="product-card" style="left:407px;top:526px"><div class="product-photo photo-zip" role="img" aria-label="Navy baby boot with orange strap and zip"></div><p class="product-name">Product Name Or<br>Number</p><p class="product-price">$399</p></article>
  <article class="product-card" style="left:615px;top:526px"><div class="product-photo photo-teal" role="img" aria-label="Teal strap baby shoe"></div><p class="product-name">Product Name Or<br>Number</p><p class="product-price">$399</p></article>
  <article class="product-card" style="left:821px;top:526px"><div class="product-photo photo-navy" role="img" aria-label="Navy lace-up baby sneaker"></div><p class="product-name">Product Name Or<br>Number</p><p class="product-price">$399</p></article>

  <article class="product-card" style="left:202px;top:792px"><div class="product-photo photo-navy" role="img" aria-label="Navy lace-up baby sneaker"></div><p class="product-name">Product Name Or<br>Number</p><p class="product-price">$399</p></article>
  <article class="product-card" style="left:407px;top:792px"><div class="product-photo photo-zip" role="img" aria-label="Navy baby boot with orange strap and zip"></div><p class="product-name">Product Name Or<br>Number</p><p class="product-price">$399</p></article>
  <article class="product-card" style="left:615px;top:792px"><div class="product-photo photo-teal" role="img" aria-label="Teal strap baby shoe"></div><p class="product-name">Product Name Or<br>Number</p><p class="product-price">$399</p></article>
  <article class="product-card" style="left:821px;top:792px"><div class="product-photo photo-navy" role="img" aria-label="Navy lace-up baby sneaker"></div><p class="product-name">Product Name Or<br>Number</p><p class="product-price">$399</p></article>

  <footer class="site-footer">
    <p class="legal">your Style 2012 © All Rights Reserved. &nbsp;|&nbsp; <a href="#">Privacy Policy</a></p>
    <p class="links"><a href="#">Home</a> &nbsp;|&nbsp; <a href="#">Advertising</a> &nbsp;|&nbsp; <a href="#">About</a> &nbsp;|&nbsp; <a href="#">Contact</a></p>
  </footer>

  <div class="bottom-stripe"></div>
</body>
</html>
```